Business Card Design Project

We are not a new company, but renamed to "Norvanta Kitchens" last year. We specialize in modern high-end cabinetry imports. We would like to communicate a sense of quality and cutting edge technology. Ideally the design would incorporate our logo colors, silver, red and preferably a black, matte background. Though we are open to suggestions.
Logo is attached.
Edit: I have attached rough drafts of the previous cards, this way you will have all necessary content that needs to go on the cards.
Reason: We have received a lot of great designs, but due to the sheer number we couldn't respond to all. We will extend the deadline for another 7 days to finalize and provide feedback to designers.
Thank you for your hard work!
Industry/Entity Type
Business
Look and feel
Each slider illustrates characteristics of the customer's brand and the style your logo design should communicate.

```html
<!DOCTYPE html>
<html lang="en">
<head>
<meta charset="UTF-8">
<title>Norvanta Kitchens — Business Cards</title>
<link href="https://fonts.googleapis.com/css2?family=Michroma&display=swap" rel="stylesheet">
<style>
  :root {
    --backdrop: #5a5c60;
    --card-navy: #151a26;
    --card-navy-deep: #0f131c;
    --silver: #cfd2d6;
    --silver-dim: #a9adb3;
    --white: #f2f3f5;
    --accent-red: #d3172b;
  }
  * { margin: 0; padding: 0; box-sizing: border-box; }
  html, body {
    width: 1200px;
    height: 900px;
    overflow: hidden;
    background: var(--backdrop);
    font-family: "Michroma", sans-serif;
  }
  .sheet {
    width: 1200px;
    height: 900px;
    display: flex;
    flex-direction: column;
    align-items: center;
    justify-content: center;
    gap: 56px;
  }
  .card {
    position: relative;
    width: 600px;
    height: 343px;
    background: linear-gradient(160deg, var(--card-navy) 0%, var(--card-navy-deep) 100%);
    border-radius: 3px;
  }

  /* Back of the card: centred wordmark */
  .card-back {
    display: flex;
    align-items: center;
    justify-content: center;
    gap: 16px;
  }
  .card-back .mark-square {
    width: 26px;
    height: 26px;
    background: var(--silver);
  }
  .card-back .wordmark {
    font-size: 27px;
    color: var(--silver);
    letter-spacing: 0.02em;
  }

  /* Front of the card */
  .card-front .wordmark-front {
    position: absolute;
    top: 88px;
    right: 40px;
    font-size: 19px;
    color: var(--silver);
    letter-spacing: 0.02em;
  }
  .identity {
    position: absolute;
    top: 42px;
    left: 36px;
  }
  .person-name {
    font-size: 15px;
    color: var(--accent-red);
    letter-spacing: 0.04em;
  }
  .person-role {
    margin-top: 4px;
    font-size: 9px;
    color: var(--white);
    letter-spacing: 0.08em;
    text-transform: uppercase;
  }
  .phones {
    margin-top: 12px;
    list-style: none;
    font-size: 10px;
    line-height: 1.75;
    color: var(--white);
    letter-spacing: 0.05em;
  }
  .phones .label {
    color: var(--accent-red);
    display: inline-block;
    width: 16px;
  }
  .divider {
    position: absolute;
    top: 198px;
    left: 0;
    width: 470px;
    height: 1px;
    background: var(--accent-red);
  }
  .details {
    position: absolute;
    top: 222px;
    left: 214px;
    font-size: 10px;
    line-height: 1.75;
    color: var(--white);
    letter-spacing: 0.05em;
  }
  .details .row {
    display: flex;
    align-items: flex-start;
  }
  .details .label {
    color: var(--accent-red);
    display: inline-block;
    width: 16px;
    flex: none;
  }
  .details .pin {
    width: 16px;
    flex: none;
    padding-top: 3px;
  }
</style>
</head>
<body>
  <main class="sheet">
    <section class="card card-back" aria-label="Card back">
      <span class="mark-square" aria-hidden="true"></span>
      <span class="wordmark">Norvanta Kitchens</span>
    </section>

    <section class="card card-front" aria-label="Card front">
      <div class="identity">
        <p class="person-name">Marcus Delane</p>
        <p class="person-role">Director</p>
        <ul class="phones">
          <li><span class="label">P</span>780 555 0142</li>
          <li><span class="label">F</span>780 555 0187</li>
          <li><span class="label">C</span>780 555 0263</li>
        </ul>
      </div>

      <p class="wordmark-front">Norvanta Kitchens</p>

      <div class="divider" aria-hidden="true"></div>

      <div class="details">
        <p class="row"><span class="label">E</span>marcus@norvantakitchens.ca</p>
        <div class="row">
          <span class="pin">
            <svg width="9" height="12" viewBox="0 0 9 12" aria-hidden="true">
              <path d="M4.5 0C2 0 0 2 0 4.4 0 7.6 4.5 12 4.5 12S9 7.6 9 4.4C9 2 7 0 4.5 0Z" fill="#d3172b"/>
              <circle cx="4.5" cy="4.4" r="1.6" fill="#151a26"/>
            </svg>
          </span>
          <span>2915 - 86 St.<br>Riverton, AB T5K 2R4</span>
        </div>
      </div>
    </section>
  </main>
</body>
</html>
```